Modern looking signage for dental office.

Exterior signage for passing cars
Target Market(s)
Cars passing by
Font styles to use
Sans Serif
Colors
3276b5
Requirements
Must have
- Logo
- OPEN ON SUTURDAY AND SUNDAY
- NIGHT CLINIC AVAILABLE
- PLEASE USE THE FONT TYPE IN FILE 4 UPLOADED BELOW.
- (482) 730-2964
- Modern looking

```html
<!DOCTYPE html>
<html lang="en">
<head>
<meta charset="utf-8">
<title>Nova Dental – Weekend &amp; Night Clinic Sign</title>
<link rel="stylesheet" href="https://fonts.googleapis.com/css2?family=Montserrat:wght@400;700&family=Open+Sans:wdth,wght@75..100,400&display=swap">
<style>
  :root {
    --frame: #5a5b5d;
    --sign: #ffffff;
    --brand-blue: #3276b5;
    --ink: #4d4a4b;
    --ink-soft: #5b5758;
    --swoosh-light: #f2f2f3;
    --swoosh-dark: #9d9ea2;
  }
  * { margin: 0; padding: 0; box-sizing: border-box; }
  html, body {
    width: 1200px; height: 1200px; overflow: hidden;
    background: var(--frame);
  }
  .sign {
    position: absolute; left: 126px; top: 124px;
    width: 952px; height: 952px;
    background: var(--sign); overflow: hidden;
  }
  .sign__wave { position: absolute; inset: 0; width: 100%; height: 100%; }
  .brand-mark {
    position: absolute; left: 58px; top: 54px;
    width: 178px; height: 178px;
    border: 2px solid var(--ink); border-radius: 50%;
  }
  .brand-name {
    position: absolute; left: 256px; top: 92px;
    font-family: "Montserrat", sans-serif; font-weight: 400;
    font-size: 86px; line-height: 1; letter-spacing: -1px;
    color: var(--ink); white-space: nowrap;
  }
  .brand-tagline {
    position: absolute; left: 319px; top: 206px;
    font-family: "Open Sans", sans-serif; font-weight: 400;
    font-stretch: 75%; font-size: 47px; line-height: 1;
    color: var(--ink-soft); white-space: nowrap;
  }
  .message { position: absolute; left: 70px; color: #fff; white-space: nowrap; }
  .message--days {
    top: 396px;
    font-family: "Montserrat", sans-serif; font-weight: 400;
    font-size: 59px; line-height: 64px; letter-spacing: 1px;
  }
  .message--night {
    top: 588px;
    font-family: "Open Sans", sans-serif; font-weight: 400;
    font-stretch: 87.5%; font-size: 51px; line-height: 1; letter-spacing: -1px;
  }
  .contact { position: absolute; left: 66px; top: 772px; color: #fff; }
  .contact__label {
    font-family: "Montserrat", sans-serif; font-weight: 700;
    font-size: 38px; line-height: 1; margin-left: 4px;
  }
  .contact__line { display: flex; align-items: center; gap: 10px; margin-top: 20px; }
  .contact__icon { width: 56px; height: 56px; }
  .contact__phone {
    font-family: "Montserrat", sans-serif; font-weight: 400;
    font-size: 50px; line-height: 1; letter-spacing: 1px;
  }
</style>
</head>
<body>
  <main class="sign">
    <svg class="sign__wave" viewBox="0 0 1191 1190" preserveAspectRatio="none" aria-hidden="true">
      <defs>
        <linearGradient id="swoosh" x1="0" y1="0" x2="0" y2="1">
          <stop offset="0" stop-color="var(--swoosh-light)"/>
          <stop offset="1" stop-color="var(--swoosh-dark)"/>
        </linearGradient>
        <linearGradient id="swoosh-top" x1="0" y1="0" x2="1" y2="0">
          <stop offset="0" stop-color="#ffffff"/>
          <stop offset="1" stop-color="#dcdcde"/>
        </linearGradient>
      </defs>
      <path fill="url(#swoosh-top)" d="M653,390 C850,470 1050,470 1188,378 L1188,410 C1130,445 1115,470 1110,480 C950,500 800,450 653,390 Z"/>
      <path fill="url(#swoosh)" d="M1043,492 C1080,700 1040,950 800,1100 C700,1160 600,1190 480,1190 L790,1190 C1000,1080 1130,900 1125,640 C1122,560 1115,500 1110,480 Z"/>
      <path fill="var(--brand-blue)" d="M0,405 C120,360 250,330 330,345 C520,360 700,470 880,490 C960,497 1000,500 1043,492 C1080,700 1040,950 800,1100 C700,1160 600,1190 480,1190 L0,1190 Z"/>
    </svg>

    <div class="brand-mark" aria-hidden="true"></div>
    <h1 class="brand-name">NOVA DENTAL</h1>
    <p class="brand-tagline">MODERN GENERAL DENTISTRY</p>

    <p class="message message--days">OPEN ON<br>SATURDAY &amp; SUNDAY</p>
    <p class="message message--night">NIGHT CLINIC AVAILABLE</p>

    <div class="contact">
      <p class="contact__label">Call :</p>
      <div class="contact__line">
        <svg class="contact__icon" viewBox="0 0 24 24" aria-hidden="true">
          <path fill="#fff" d="M6.6 2.5c.5-.3 1.1-.1 1.4.4l2 3.4c.3.5.2 1.1-.2 1.4L8.3 8.8c.9 2.6 2.8 4.9 5.3 6.2l1.2-1.5c.4-.4 1-.5 1.4-.2l3.3 2.1c.5.3.6 1 .3 1.4l-1.5 2.3c-.6.9-1.7 1.3-2.7 1C9.4 18.4 4.9 13.1 3.6 7c-.2-1 .3-2 1.1-2.6z"/>
          <path fill="none" stroke="#fff" stroke-width="1.4" stroke-linecap="round" d="M14 7.5a3 3 0 0 1 2.5 2.5M14.2 4.6a6 6 0 0 1 5.2 5.2M14.4 1.8a9 9 0 0 1 7.8 7.8"/>
        </svg>
        <span class="contact__phone">(482) 730-2964</span>
      </div>
    </div>
  </main>
</body>
</html>
```